FLY/CRUISE PACAKGE TO THE ARCTIC TO SEE BIRD LIFE and POLAR BEARS

I am wanting to create a double sided A4 colour flyer (Finished size: 297 x 210mm) for a Fly/Cruise package from Australia to the Arctic.
The idea is that I would like the art work or design work done for the flyer that I can then send to a printer to do the printing of these flyers.

My business is a retail cruise travel agent that specializes in selling all-inclusive packages on luxury expedition ships and in this case I intend to promote this cruise to people that are interested in wildlife and also bird watching.

I will attach a copy of the full brochure from the cruise line Meridane Voyages that we will be using to give you more information on them and the cruise we are travelling on will be on page 38 and 39 of the brochure and I show you this because it gives you a map of the cruise.

I will also attach my logo so this can be included and a copy of the draft itinerary that I see as being the highlights however I am aware that we are limited on space and we need to get the key issues across and also as the trip is being marketed to bird watchers and wildlife enthusiasts then some good pictures of both a polar bear and let’s say a bird called a puffin and maybe a Reindeer.

We also need to show the costing's and what's included in the package.

And of course a call to action
All bookings and enquiries call Corbin

1-300-418-937
WavePath Pty Ltd

“I never forget you have a choice”

Target Market(s)

Travellers that are interested in Expedition cruising and are keen on seeing wildlife and birdlife

Industry/Entity Type

Travel Industry

Colors
0255a3
ec1f27
ffffff
0393ce

Requirements
Must have
• A picture od a Polar Bear / A Puffin
• It must look very professional as this trip is an expensive trip
Nice to have
• A picture of the ship "Tern Harbour"
• Bright and appealing appearance
• See the Polar Bears while officials still allow tourism to this area

```html
<!DOCTYPE html>
<html lang="en">
<head>
<meta charset="utf-8">
<title>West Spitsbergen &amp; Polar Ice Edge Cruise Flyer</title>
<link href="https://fonts.googleapis.com/css2?family=Open+Sans:ital,wght@0,400;0,600;0,700;1,400;1,700&family=Tinos:wght@700&family=Kalam&display=swap" rel="stylesheet">
<style>
:root{
  --navy:#0255a3;
  --red:#ec1f27;
  --white:#ffffff;
  --sky:#0393ce;
  --ink:#333;
  --stage:#ececec;
}
*{box-sizing:border-box;margin:0;padding:0}
html,body{width:1200px;height:845px;overflow:hidden;background:var(--stage);font-family:"Open Sans",sans-serif;color:var(--ink)}
.page{position:absolute;top:22px;width:546px;height:772px;background:var(--white);box-shadow:0 3px 10px rgba(0,0,0,.35);overflow:hidden}
.page--front{left:36px}
.page--back{left:615px}

/* front */
.hero{position:absolute;left:0;top:0;width:546px;height:298px;background:linear-gradient(180deg,#e9dfd3 0%,#dfe6ee 40%,#bcd1e6 70%,#e9eff5 100%)}
.brand-mark{position:absolute;left:46px;top:40px;width:55px;height:84px;background:var(--navy);border:2px solid #fff;outline:1px solid var(--navy)}
.title{position:absolute;left:126px;top:38px;font-family:"Tinos",serif;font-weight:700;color:#1d4f9a;font-size:29px;line-height:33px;letter-spacing:.3px;white-space:nowrap}
.dates{position:absolute;left:126px;top:104px;color:var(--red);font-size:17px;white-space:nowrap}
.panel{position:absolute;left:0;top:298px;width:546px;height:450px;background:linear-gradient(180deg,#0a72c4 0%,#0393ce 55%,#0a6cbe 100%)}
.thumb{position:absolute;left:32px;width:166px}
.thumb--reindeer{top:322px;height:120px;border-radius:14px 0 0 0;background:linear-gradient(180deg,#8aa3c6 0%,#c9d4e0 45%,#8c7a66 100%)}
.thumb--puffin{top:446px;height:119px;background:linear-gradient(180deg,#a9c0dc,#dbe6f1)}
.thumb--fox{top:570px;height:119px;border-radius:0 0 24px 0;background:linear-gradient(180deg,#dfe5ec,#f4f6f8)}
.intro{position:absolute;left:223px;top:325px;width:294px;color:#fff;font-size:9.1px;line-height:12px;text-align:justify;letter-spacing:-.05px}
.intro p{margin-bottom:4px}
.intro em{font-weight:700}
.swoosh{position:absolute;left:0;top:695px}
.front-foot{position:absolute;left:0;top:722px;width:546px;height:50px}
.wordmark{font-family:"Open Sans",sans-serif;font-weight:700;color:var(--navy);letter-spacing:.5px;display:flex;align-items:center;gap:6px;white-space:nowrap}
.wordmark i{display:inline-block;border-radius:50%;background:var(--navy)}
.front-foot .wordmark{position:absolute;left:186px;top:10px;font-size:20px}
.front-foot .wordmark i{width:14px;height:14px}

/* back */
.map{position:absolute;left:27px;top:12px;width:138px;height:120px;border:1px solid #555;background:linear-gradient(160deg,#f2f6fa,#d7e6f2);z-index:2}
.url{position:absolute;left:177px;top:26px;font-size:11.5px;color:#666}
.band{position:absolute;left:0;top:46px;width:421px;height:72px;background:var(--sky);color:#fff;padding:14px 0 0 177px;white-space:nowrap}
.band .sub{font-size:13.5px;line-height:17px}
.band .main{font-size:20px;line-height:26px;letter-spacing:.2px}
.strip{position:absolute;left:421px;width:125px}
.strip--ship{top:0;height:258px;background:linear-gradient(180deg,#c7d9ea 0%,#e8eef4 45%,#23477a 80%,#1b3a66 100%)}
.strip--guests{top:262px;height:247px;background:linear-gradient(160deg,#5e4a3c,#b46b3a 50%,#c7231f 100%)}
.strip--bear{top:513px;height:259px;background:linear-gradient(180deg,#2f78bd 0%,#8fb8dd 45%,#f1f4f8 75%,#c7231f 100%)}
.itinerary{position:absolute;left:30px;top:148px;width:371px;font-size:8px;line-height:10.9px;text-align:justify;color:#444;letter-spacing:-.05px}
.itinerary p{margin-bottom:6px}
.itinerary .lead{font-style:italic}
.itinerary b{color:var(--red);font-weight:600}
.tab{display:inline-block;background:var(--sky);color:#fff;font-weight:700;font-size:10px;line-height:13px;padding:0 16px 0 10px;clip-path:polygon(0 0,100% 0,88% 100%,0 100%)}
.rates{position:absolute;left:31px;top:508px;width:125px;font-size:8px;line-height:11px;color:#444}
.rates p{margin-top:6px}
.rates .it{font-style:italic}
.rates strong{font-weight:600;color:#333}
.inclusions{position:absolute;left:166px;top:508px;width:240px;font-size:8px;line-height:11px;color:#444}
.inclusions p{margin-top:6px}
.contact{position:absolute;left:166px;top:613px;width:180px;font-size:8px;line-height:11px;color:#444}
.contact .it{font-style:italic;margin-top:6px}
.contact .who{margin-top:6px;white-space:nowrap}
.contact .who strong{font-weight:600;color:#333}
.badge{position:absolute;left:347px;top:614px;width:52px;height:38px;border-radius:4px;background:#b9c2cc}
.lines{position:absolute;left:166px;top:664px;display:flex;gap:14px;font-size:9.5px;color:#333;align-items:center;white-space:nowrap}
.lines span{display:flex;align-items:center;gap:5px}
.page--back .wordmark{position:absolute;left:190px;top:696px;font-size:19px}
.page--back .wordmark i{width:13px;height:13px}
.quote{position:absolute;left:74px;top:736px;font-family:"Kalam",cursive;font-size:14px;color:#2a6fb8;white-space:nowrap}
</style>
</head>
<body>

<section class="page page--front">
  <div class="hero" role="img" aria-label="Polar bear walking across snow and pack ice under a pale Arctic sky"></div>
  <div class="brand-mark" aria-hidden="true"></div>
  <h1 class="title">WEST SPITSBERGEN<br>&amp; POLAR ICE EDGE CRUISE</h1>
  <p class="dates">27 JUN - 05 JUL 2018,&nbsp; Aboard M/v “Tern Harbour”</p>

  <div class="panel"></div>
  <div class="thumb thumb--reindeer" role="img" aria-label="Reindeer grazing on tundra before snowy mountains"></div>
  <div class="thumb thumb--puffin" role="img" aria-label="Atlantic puffin in flight with wings spread"></div>
  <div class="thumb thumb--fox" role="img" aria-label="White Arctic fox in the snow"></div>
  <div class="intro">
    <p><em>Exploration of West Spitsbergen</em> is the main part of this special cruise. It is a real expedition in a true High Arctic wilderness. As such, our route and exploration opportunities here are heavily dependent on the weather and sea ice conditions we encounter. Our experienced captain and expedition leader decide the itinerary and continually adjust plans as conditions and opportunities warrant. Best possible advantage will be taken of the circumstances presented to us by the Nature of the Arctic.</p>
    <p>There are spectacular fjords, coasts, and islands in the north-western part of Svalbard. <em>This area contains the archipelago’s most impressive scenery and some of the Arctic’s best wildlife viewing opportunities.</em> On ice floes and on fast ice several species of seals watch vigilantly for polar bears. Fields of flowering tundra are home to grazing reindeer and playful Arctic fox. Bountiful inshore and offshore waters are home to walrus and a wide variety of whales. The whole area is alive with migratory birds, including numerous rare species, taking advantage of summer’s fecundity in 24-hour daylight.</p>
    <p>And over it all presides the polar bear, monarch of the North. This wild corner of Svalbard is <em>one of the best places in the world to observe polar bears</em> in their preferred habitat: the pack ice. We take the ship as close as safely possible to the jumbled and broken edge of the polar ice cap, where polar bears stalk the frozen sea.</p>
    <p>The area of exploration also contains the historical remnants of whaling camps, coal mining operations, trappers’ cabins, staging areas for historic attempts to discover the North Pole, and even an abandoned polar research station. Human habitation in this area can be found only at Ny Ålesund, a former mining town that is now home to an international community of Arctic researchers.</p>
  </div>

  <svg class="swoosh" width="546" height="77" viewBox="0 0 546 77" aria-hidden="true">
    <path d="M0 40 Q273 0 546 8 V77 H0 Z" fill="#fff"/>
    <path d="M0 34 Q273 -6 546 2 V10 Q273 4 0 44 Z" fill="var(--red)"/>
  </svg>
  <div class="front-foot">
    <div class="wordmark"><i></i>WAVEPATH</div>
  </div>
</section>

<section class="page page--back">
  <div class="map" role="img" aria-label="Route map of Svalbard showing the cruise track from Longyearbyen around West Spitsbergen"></div>
  <div class="url">www.wavepath.com.au</div>
  <div class="band">
    <div class="sub">West Spitsbergen &amp; Polar Ice Edge</div>
    <div class="main">THE CRUISE HIGHLIGHTS</div>
  </div>

  <div class="strip strip--ship" role="img" aria-label="Expedition ship beside a towering iceberg"></div>
  <div class="strip strip--guests" role="img" aria-label="Guests in red parkas watching from the deck rail"></div>
  <div class="strip strip--bear" role="img" aria-label="Polar bear standing on top of an ice ridge with guests in red below"></div>

  <div class="itinerary">
    <p class="lead">Sunday 24th June we Fly from our Home Australian airport to Singapore. Check-in 24 June out 26 June with late check out on the 26th (Return airport transfers, Full breakfast, City Tour, Dinner and nightlife tour at the Singapore Zoo). Tuesday 26th June we fly overnight from Singapore to Norway where we join are cruise package.</p>
    <p><b>DAY 1: LONGYEARBYEN, SVALBARD.</b> Welcome to Longyearbyen, the administrative capital of the Norwegian territory of Svalbard and starting point of our expedition. After arriving via scheduled commercial flight service, you are free to explore this fascinating Arctic settlement.</p>
    <p><b>DAY 2: EMBARKATION IN LONGYEARBYEN.</b> In the afternoon we welcome you aboard the luxury expedition ship M/V Tern Harbour. Explore the ship and get comfortable in your home away from home for the extraordinary adventure to come. The scenery as we sail through Isfjorden on our first evening is spectacular and there is already the possibility of marine mammal encounters.</p>
    <p><b>DAY 3-8: EXPLORATION OF WEST SPITSBERGEN.</b> Wildlife that we may have the opportunity to see on our trip pending on weather conditions. We will have daylight 24 hours each day during our cruise. 19 species of Mammal are known to be in the area that we are visiting &amp; some are: Polar Bears / Walruses / Seals / Whales / Reindeer / Arctic Fox. 30 Sea Bird species call Spitsbergen home during summer and some we are hoping to see are: Atlantic Puffin / Snow Bunting / Pink-Footed Geese / Purple Sandpiper / Ptarmigan / Common Guillemot / Arctic Terns / Black Legged Kittiwake / Great Skua and if we are very lucky we may spot the Sabine Gull or a King Elder. Whilst the above cannot be guaranteed it is know that most visitors do spot approximately 23 species during similar trips.</p>
    <p><b>DAY 9: DISEMBARKATION IN LONGYEARBYEN, SVALBARD.</b> After breakfast we say farewell in the town of Longyearbyen, where we started. We provide a transfer to the airport or to the town center if you wish to spend more time here.</p>
    <p class="lead">Thursday 5th July our cruise package finishes and we fly to our next destination: If you select to fly home to Australia we have included a 2 night stopover on the way home and you may select from Singapore or Hong Kong or Bangkok / transfers-breakfast and city tour included. Or ask for other options as the return is very flexible you may like to consider a Baltic cruise or a land based tour or a river cruise as an add on just ask us for options.</p>
  </div>

  <div class="rates">
    <span class="tab">RATES</span>
    <p class="it">Early Bird Fares available till end July 2017 or until sold out.</p>
    <p><strong>· Twin Share OUTSIDE CABIN<br>$11,999.00 per person.</strong></p>
    <p><strong>· Twin Share BALCONY CABIN<br>$13,999.00 per person.</strong></p>
    <p class="it">Single costings and costs to upgrade to a Suite on application.</p>
    <p class="it">Deposit $4,000 per person due 14days after confirmation and is non-refundable / Insurance quote will be given</p>
    <p>Final payment 01 March 2018</p>
  </div>

  <div class="inclusions">
    <span class="tab">INCLUSIONS</span>
    <p>· Return economy class airfare and taxes from your home Australian Airport · 2.5 night Hotel package in Singapore · 8 night cruise package that includes 1 nights pre-cruise hotel accommodation and the 7 night cruise · All meals and most expeditions whilst on board our ship The Tern Harbour · 2.5 night stopover package on your return trip home to Australia</p>
  </div>

  <div class="contact">
    <span class="tab">CONTACT</span>
    <p class="it">For Bookings &amp; Enquiries contact:</p>
    <p class="who"><strong>Corbin Hale</strong> - Your Personal Travel Concierge</p>
  </div>
  <div class="badge" aria-hidden="true"></div>
  <div class="lines">
    <span><svg width="16" height="16" viewBox="0 0 16 16" aria-hidden="true"><circle cx="8" cy="8" r="7" fill="none" stroke="var(--sky)" stroke-width="1.5"/><path d="M5 6c0-1 1-1.5 1.5-1.5l.8 1.6-.8.8c.4.9 1.1 1.6 2 2l.8-.8 1.6.8c0 .5-.5 1.5-1.5 1.5C7 10.4 5 8.4 5 6z" fill="var(--sky)"/></svg>1-300-418-937</span>
    <span><svg width="16" height="16" viewBox="0 0 16 16" aria-hidden="true"><circle cx="8" cy="8" r="7" fill="none" stroke="var(--sky)" stroke-width="1.5"/><rect x="4.5" y="5.5" width="7" height="5" fill="none" stroke="var(--sky)" stroke-width="1.2"/><path d="M4.5 5.5 8 8.5l3.5-3" fill="none" stroke="var(--sky)" stroke-width="1.2"/></svg>corbin@wavepath.com.au</span>
  </div>
  <div class="wordmark"><i></i>WAVEPATH</div>
  <p class="quote">“I never forget you have a choice” – Corbin Hale</p>
</section>

</body>
</html>
```